International Software Company Requires 3 Product Brochures.

Having just redesigned our website we require 3 brochures. 1 for each of our software products.
Our customers are global, blue chip, organisations and a professional, corporate style is required for each of the product brochures.
While each of the products are separate it should be clear that they are part of a family of products. All products are firmly marketed to the international oil and gas sector.
Rather than produce designs for 3 brochures straight away, we ask that designers produce a layout with a “unified theme” but with slight modifications adapted for each product. Please show the internal layout as well as the external cover.
Once we have chosen a design we will ask the designer to produce the three variations.
Designs should complement our new website design (not yet published) which can be found in the attachments section of this project.
The 3 products are…
QVT - time & cost estimation software
QVT is used by engineers to estimate the time and cost required to drill an oil or gas well. This involves modelling all the stages of drilling and then associating costs and risks to each stage before simulating the project using the Monte Carlo methodology to create a probabilistic result. The message is about delivering accurate and consistent results that communicate the project and risk to management. Attachment FJQVT1.jpg is a graphic we have previously used to illustrate the QVT process but we do not think is very effective.
LPW - materials & cost control software
LPW is used by drilling and logistics staff to keep very accurate and up-to-date track of all the costs and equipment associated with drilling a well. LPW quickly and accurately produces various cost and materials reports in what is a very complex and costly engineering project and where different departments (such as engineering or finance) have different needs. Attachment FJLPW1.jpg is a graphic we have previously used to illustrate the LPW process but we do not think is very effective.
ZHN – lessons learned software
ZHN is a web based system used by oil and gas companies to record and share lessons learned associated with drilling and maintaining wells. These are complex, expensive and often dangerous processes where it is vital that knowledge is shared between staff not matter where in the word they are located.
The brochure format we are looking for is double A4 bi-fold, (a front cover, 2 internal pages and a back page, A4 size.)
The brochures will be both printed and send out as PDFs to prospective clients.
Reason: We realise that our brief may not have been as clear as it could and a 3 brochure requirement may seem overwhelming.
We are updating the brief to ask designers to produce a layout with a “unified theme” but with slight modifications adapted for each product.
Initially we ask that designers give us an example of external and internal pages for a single product brochure as an example of the unified theme.
We are extending the deadline to allow for more entries.
We have just realised that the currency for this project was in USD and not GBP as we assumed. We have therefore substantially increased the
budget on this project, with a first place of $600-USD.
Engineers and financial staff within International oil and gas companies, i.e. GW, Pelta, Durango etc.
Oil And Gas

```html
<!DOCTYPE html>
<html lang="en">
<head>
<meta charset="utf-8">
<title>Strataline Systems – Back Covers</title>
<link rel="stylesheet" href="https://fonts.googleapis.com/css2?family=Open+Sans:wght@400;600;700&display=swap">
<style>
  :root {
    --page: #ffffff;
    --label: #b4b5b8;
    --band: #929396;
    --band-dark: #7f8083;
    --strip-light: #d3d4d6;
    --teal: #4f98a6;
    --teal-deep: #2f5f66;
    --green: #8cbf4f;
    --brand: #2d6570;
    --tag: #3a3b3e;
    --white: #ffffff;
    --partner: #c9ccd1;
    --muted: #d9dadc;
  }
  html, body {
    margin: 0;
    padding: 0;
    width: 822px;
    height: 1200px;
    overflow: hidden;
    background: var(--page);
    font-family: "Open Sans", Arial, sans-serif;
  }
  .stage {
    position: relative;
    width: 850px;
    height: 1241px;
    transform: scale(0.967);
    transform-origin: 0 0;
  }
  .sheet-label {
    position: absolute;
    left: 20px;
    font-size: 12.5px;
    letter-spacing: 0.3px;
    color: var(--label);
    margin: 0;
    font-weight: 400;
  }
  .cover {
    position: absolute;
    left: 20px;
    width: 813px;
    height: 576px;
    background: var(--page);
    box-shadow: 0 1px 4px rgba(0,0,0,0.35);
    overflow: hidden;
  }
  .brand {
    position: absolute;
    display: flex;
    align-items: center;
    gap: 8px;
    color: var(--brand);
    font-weight: 700;
    letter-spacing: 1px;
    white-space: nowrap;
  }
  .brand-dot {
    border-radius: 50%;
    background: var(--brand);
    flex: none;
  }
  .brand--top { left: 600px; top: 55px; font-size: 19px; }
  .brand--top .brand-dot { width: 34px; height: 34px; }
  .brand--band { left: 26px; top: 455px; font-size: 17px; color: var(--brand); }
  .brand--band .brand-dot { width: 30px; height: 30px; }

  .side-strip { position: absolute; width: 11px; top: 145px; left: 0; }
  .side-strip--upper { height: 226px; }
  .side-strip--lower { top: 371px; height: 205px; }
  .edge-strip { position: absolute; left: 772px; width: 33px; }
  .edge-strip--upper { top: 146px; height: 225px; }
  .edge-strip--lower { top: 371px; height: 205px; }

  .band {
    position: absolute;
    left: 0;
    top: 371px;
    width: 813px;
    height: 205px;
    background: var(--band);
  }
  .photo {
    position: absolute;
    left: 407px;
    top: 146px;
    width: 365px;
    height: 225px;
  }
  .accent { position: absolute; height: 5px; top: 366px; }
  .accent--teal { left: 407px; width: 101px; background: var(--teal); }
  .accent--green { left: 508px; width: 152px; background: var(--green); }
  .product-tag {
    position: absolute;
    left: 660px;
    top: 348px;
    width: 112px;
    height: 23px;
    background: var(--tag);
    color: var(--white);
    font-size: 21px;
    line-height: 23px;
    text-align: right;
    padding-right: 10px;
    box-sizing: border-box;
    letter-spacing: 1px;
  }
  .overlay-note {
    position: absolute;
    left: 516px;
    top: 373px;
    font-size: 12px;
    color: var(--muted);
    letter-spacing: 0.3px;
  }
  .partners-title {
    position: absolute;
    left: 33px;
    top: 316px;
    margin: 0;
    font-size: 11.5px;
    font-weight: 400;
    color: #8b8c8f;
  }
  .partners {
    position: absolute;
    left: 33px;
    top: 345px;
    margin: 0;
    padding: 0;
    list-style: none;
  }
  .partner {
    position: absolute;
    top: 0;
    height: 15px;
    border-radius: 2px;
    background: var(--partner);
  }
  .tagline {
    position: absolute;
    right: 54px;
    top: 465px;
    margin: 0;
    text-align: right;
    color: var(--white);
    font-size: 11px;
    font-weight: 600;
    letter-spacing: 1.3px;
    line-height: 15px;
    text-transform: uppercase;
  }
  .imprint {
    position: absolute;
    left: 26px;
    top: 512px;
    width: 160px;
    color: var(--white);
    font-size: 5.5px;
    line-height: 7.5px;
  }
  .imprint strong { display: block; font-weight: 700; }
  .imprint p { margin: 0; opacity: 0.85; }

  /* product variants */
  .cover--zhn .side-strip--upper { background: var(--strip-light); }
  .cover--zhn .side-strip--lower { background: var(--band-dark); }
  .cover--zhn .edge-strip--upper { background: var(--strip-light); }
  .cover--zhn .edge-strip--lower { background: var(--band-dark); }
  .cover--zhn .photo { background: linear-gradient(100deg, #eef0f2 0%, #d9dcdf 45%, #5b4a44 70%, #e9eaeb 100%); }

  .cover--lpw .side-strip--upper { background: var(--teal); }
  .cover--lpw .side-strip--lower { background: var(--teal-deep); }
  .cover--lpw .edge-strip--upper { background: var(--teal); }
  .cover--lpw .edge-strip--lower { background: var(--teal-deep); }
  .cover--lpw .photo { background: linear-gradient(95deg, #f4f5f6 0%, #e3e5e7 50%, #3c3e42 78%, #ecedee 100%); }
</style>
</head>
<body>
<div class="stage">

  <h2 class="sheet-label" style="top:26px;">ZHN BACK COVER</h2>
  <section class="cover cover--zhn" style="top:52px;">
    <div class="brand brand--top"><span class="brand-dot"></span>STRATALINE</div>
    <div class="side-strip side-strip--upper"></div>
    <div class="band"></div>
    <div class="side-strip side-strip--lower"></div>
    <div class="edge-strip edge-strip--upper"></div>
    <div class="edge-strip edge-strip--lower"></div>
    <div class="photo" role="img" aria-label="Photo of a smiling businesswoman working at a laptop in a bright office"></div>
    <div class="accent accent--teal"></div>
    <div class="accent accent--green"></div>
    <div class="product-tag">ZHN</div>
    <span class="overlay-note">LPW COVER</span>
    <h3 class="partners-title">Our partners</h3>
    <ul class="partners" aria-label="Partner badges">
      <li class="partner" style="left:0;width:16px;"></li>
      <li class="partner" style="left:48px;width:12px;"></li>
      <li class="partner" style="left:84px;width:26px;"></li>
      <li class="partner" style="left:124px;width:38px;"></li>
      <li class="partner" style="left:180px;width:12px;border-radius:50%;"></li>
      <li class="partner" style="left:219px;width:18px;"></li>
      <li class="partner" style="left:262px;width:22px;"></li>
      <li class="partner" style="left:308px;width:16px;"></li>
    </ul>
    <div class="brand brand--band"><span class="brand-dot"></span>STRATALINE</div>
    <div class="imprint">
      <strong>Strataline Systems</strong>
      <p>Drilling data tools built for engineers, finance teams and field staff working on wells around the world, every day.</p>
    </div>
    <p class="tagline">Lessons learned software</p>
  </section>

  <h2 class="sheet-label" style="top:639px;">LPW BACK COVER</h2>
  <section class="cover cover--lpw" style="top:659px;">
    <div class="brand brand--top"><span class="brand-dot"></span>STRATALINE</div>
    <div class="side-strip side-strip--upper"></div>
    <div class="band"></div>
    <div class="side-strip side-strip--lower"></div>
    <div class="edge-strip edge-strip--upper"></div>
    <div class="edge-strip edge-strip--lower"></div>
    <div class="photo" role="img" aria-label="Photo of a businessman sketching a network of connected people and devices on a glass board"></div>
    <div class="accent accent--green" style="left:508px;"></div>
    <div class="product-tag" style="background:var(--tag);">LPW</div>
    <h3 class="partners-title">Our partners</h3>
    <ul class="partners" aria-label="Partner badges">
      <li class="partner" style="left:0;width:16px;"></li>
      <li class="partner" style="left:48px;width:12px;"></li>
      <li class="partner" style="left:84px;width:26px;"></li>
      <li class="partner" style="left:124px;width:38px;"></li>
      <li class="partner" style="left:180px;width:12px;border-radius:50%;"></li>
      <li class="partner" style="left:219px;width:18px;"></li>
      <li class="partner" style="left:262px;width:22px;"></li>
      <li class="partner" style="left:308px;width:16px;"></li>
    </ul>
    <div class="brand brand--band"><span class="brand-dot"></span>STRATALINE</div>
    <div class="imprint">
      <strong>Strataline Systems</strong>
      <p>Drilling data tools built for engineers, finance teams and field staff working on wells around the world, every day.</p>
    </div>
    <p class="tagline" style="top:465px;">Cost tracking<br>&amp; reporting software</p>
  </section>

</div>
</body>
</html>
```